QuarryNest - Webstartup looking for some style

QuarryNest is a cloud based web application that allows construction sub-contractors to create and manage bids. Generally, these contractors will contact subcontractors to have them do specific parts of a larger construction project. This would be used by various subcontractors including woodwork (cabinetry), electricians, masons, etc...

Nearly all competitors are clients applications that have to be installed on the computer and are very expensive. This is a much lower cost alternative.

The business is just beginning and we want people to view us as a fresh alternative to companies that have been around for a long time and are starting to look a little dated.

We would like our logo included on the card (see attached). We have been using the circular 'qn' emblem seperately from the complete logo in various areas of the website. We lean towards a professional and clean look, with a tendancy more towards modern.

We want to differentiate ourselves from our competition which tend to be dated, complicated and less graphical.

(We are currently designing our public website as well - but don't have any designs yet)

Industry/Entity Type

Construction

Requirements
Must have
• Circular 'qn' emblem from logo. Probably entire logo, but not necessarily.

Should have reference to website: www.quarrynest-demo.net

The Url should be all lowercase (www.quarrynest-demo.net)
Should not have
• we do not want to list a phone number or email address on the cards. we want people to go to the actual website. we haven't decided if we want names printed on the business cards.

```html
<!DOCTYPE html>
<html lang="en">
<head>
<meta charset="utf-8">
<title>QuarryNest Business Card</title>
<link rel="stylesheet" href="https://fonts.googleapis.com/css2?family=Arimo:wght@400;700&display=swap">
<style>
  :root {
    --page-bg: #ffffff;
    --blue-deep: #0a6db4;
    --blue-mid: #1f8fd3;
    --blue-light: #29abe2;
    --orange: #f7941d;
    --orange-light: #fbb040;
    --text-grey: #6d6e71;
    --card-border: #d9d9d9;
    --white: #ffffff;
  }
  * { margin: 0; padding: 0; box-sizing: border-box; }
  html, body {
    width: 1200px;
    height: 900px;
    overflow: hidden;
    background: var(--page-bg);
    font-family: "Arimo", Arial, sans-serif;
  }
  .canvas {
    position: relative;
    width: 1200px;
    height: 900px;
  }
  .card {
    position: absolute;
    top: 162px;
    width: 320px;
    height: 576px;
    border-radius: 18px;
    overflow: hidden;
    box-shadow: 2px 3px 5px rgba(0,0,0,0.22);
  }
  .card-back {
    left: 256px;
    background: linear-gradient(180deg, var(--blue-deep) 0%, var(--blue-mid) 35%, var(--blue-light) 70%, var(--blue-light) 100%);
  }
  .card-front {
    left: 624px;
    background: var(--white);
    border: 1px solid var(--card-border);
  }
  .emblem-block {
    position: absolute;
    left: 0;
    right: 0;
    top: 222px;
    display: flex;
    flex-direction: column;
    align-items: center;
    gap: 10px;
  }
  .emblem-circle {
    width: 96px;
    height: 96px;
    border-radius: 50%;
    background: var(--white);
  }
  .emblem-name {
    color: var(--white);
    font-size: 22px;
    font-weight: 700;
  }
  .url-band {
    position: absolute;
    left: 0;
    right: 0;
    top: 482px;
    height: 48px;
    display: flex;
    align-items: center;
    justify-content: center;
    color: var(--white);
    font-size: 21px;
    font-weight: 700;
    letter-spacing: 0.2px;
  }
  .card-back .url-band {
    background: linear-gradient(90deg, var(--orange) 0%, var(--orange-light) 50%, var(--orange) 100%);
  }
  .card-front .url-band {
    top: 481px;
    background: linear-gradient(90deg, var(--blue-mid) 0%, var(--blue-light) 50%, var(--blue-mid) 100%);
  }
  .brand {
    position: absolute;
    top: 46px;
    left: 0;
    right: 0;
    display: flex;
    align-items: center;
    justify-content: center;
    gap: 10px;
  }
  .brand-dot {
    width: 50px;
    height: 50px;
    border-radius: 50%;
    background: var(--blue-mid);
  }
  .brand-name {
    color: var(--blue-mid);
    font-size: 34px;
    font-weight: 400;
  }
  .person {
    position: absolute;
    top: 263px;
    left: 0;
    right: 0;
    text-align: center;
    color: var(--text-grey);
  }
  .person-name {
    font-size: 23px;
    font-weight: 400;
  }
  .person-name strong { font-weight: 700; }
  .person-role {
    margin-top: 5px;
    font-size: 15px;
  }
  .address {
    position: absolute;
    top: 418px;
    left: 0;
    right: 0;
    text-align: center;
    color: var(--text-grey);
    font-size: 15.5px;
    line-height: 23px;
  }
</style>
</head>
<body>
<main class="canvas">
  <section class="card card-back">
    <div class="emblem-block">
      <div class="emblem-circle"></div>
      <span class="emblem-name">QuarryNest</span>
    </div>
    <div class="url-band">www.quarrynest-demo.net</div>
  </section>

  <section class="card card-front">
    <div class="brand">
      <div class="brand-dot"></div>
      <span class="brand-name">QuarryNest</span>
    </div>
    <div class="person">
      <p class="person-name">Daniel R. <strong>Hartley</strong></p>
      <p class="person-role">Business Development</p>
    </div>
    <address class="address" style="font-style:normal">
      1207 Cedar Lane<br>
      Marlow, ND 58012
    </address>
    <div class="url-band">www.quarrynest-demo.net</div>
  </section>
</main>
</body>
</html>
```